Eye surgeon needs a presentation folder and a business card for his practice manager. Logo alread...

I need a folder to put papers in when I am scheduling patients for surgery. The information is general, such as costs, consent forms etc. The folder is designed to give the patient these papers in a neat manner. The cover of the folder needs to use my brand and perhaps create some interest when it is sitting on their kitchen bench with visitors and family. I'll attach a typical template for a folder. It needs to be stylish, classic and professional, as I am about to operate on the person's eye. <br/>I would like my logo included. I'll also attach a photo which is on my website which might work to wrap around the folder. The website address is raybelford.com.au and you can see the way the image is used there on most of the pages as a banner. My profile photo could possibly used as well. Perhaps on the back, but if it looks strange then that is not necessary. The contact information need not be on the folder. Just Dr Ray Belford, Ophthalmic Surgeon. Finally, our brand slogan is. "The world's a beautiful place, see it clearly". This could also be on it. Again, this all needs to be professional looking. <br/>I've attached all our previous design jobs, 2 profile pictures, and the image that I think would work. Please also look at the website. <br/><br/>The second part of the project is to create a business card for my practice manager. Her name is Miriam Holtby<br/>It should include<br/>Miriam Holtby (BCom)<br/>Practice Manager for Dr Ray Belford<br/>Ophthalmic Surgeon <br/><br/>Then all the details which are on our current business card<br/><br/><br/><br/><br/>

Contact Information for Business Card

Just match the business cards I already have, but use the details above

Colors

Designer to choose colors to be used in the design.

```html
<!DOCTYPE html>
<html lang="en">
<head>
<meta charset="utf-8">
<title>Business Card – Miriam Holtby</title>
<link rel="stylesheet" href="https://fonts.googleapis.com/css2?family=Tinos:wght@400;700&family=Arimo:wght@400&display=swap">
<style>
  :root {
    --ink: #4a4a4a;
    --ink-soft: #555555;
    --brand-blue: #2a7fc4;
    --brand-blue-deep: #1f6fb3;
    --brand-blue-light: #3aa2d8;
    --silver: #b8b8b8;
    --paper: #ffffff;
  }
  * { margin: 0; padding: 0; box-sizing: border-box; }
  html, body { width: 1200px; height: 686px; overflow: hidden; background: var(--paper); }
  .card {
    position: relative;
    width: 1200px;
    height: 686px;
    background: var(--paper);
    overflow: hidden;
    color: var(--ink);
  }
  .identity { position: absolute; left: 68px; top: 72px; font-family: "Tinos", "Times New Roman", serif; }
  .identity__name { font-weight: 700; font-size: 49px; line-height: 1; letter-spacing: 0.3px; color: var(--ink); }
  .identity__role { font-size: 39px; line-height: 51px; margin-top: 14px; color: var(--ink-soft); }
  .identity__specialty { font-size: 36px; line-height: 1; margin-top: 8px; color: var(--ink-soft); transform: scaleX(0.88); transform-origin: left; }

  .brand { position: absolute; left: 880px; top: 110px; display: flex; align-items: center; gap: 16px; }
  .brand__dot { width: 54px; height: 54px; border-radius: 50%; background: var(--brand-blue); flex: none; }
  .brand__name { font-family: "Tinos", "Times New Roman", serif; font-size: 38px; font-weight: 400; line-height: 1.05; color: var(--brand-blue); }

  .contact { position: absolute; left: 63px; top: 458px; font-family: "Arimo", Arial, sans-serif; color: var(--ink-soft); list-style: none; }
  .contact__item { display: flex; align-items: center; height: 52px; font-size: 40px; }
  .contact__item--email { margin-top: 4px; }
  .contact__icon { width: 40px; height: 40px; margin-right: 16px; flex: none; }

  .address { position: absolute; right: 41px; top: 508px; font-family: "Arimo", Arial, sans-serif; font-size: 40px; line-height: 51px; text-align: right; color: var(--ink-soft); }

  .footer-band { position: absolute; left: 0; bottom: 0; width: 1200px; height: 50px; }
</style>
</head>
<body>
<main class="card">
  <section class="identity">
    <h1 class="identity__name">Miriam Holtby (BCom)</h1>
    <p class="identity__role">Practice Manager for<br>Dr Ray Belford</p>
    <p class="identity__specialty">Ophthalmic Surgeon</p>
  </section>

  <div class="brand">
    <span class="brand__dot"></span>
    <span class="brand__name">Belford<br>Eye Care</span>
  </div>

  <ul class="contact">
    <li class="contact__item">
      <svg class="contact__icon" viewBox="0 0 40 40" aria-hidden="true">
        <circle cx="20" cy="20" r="19" fill="var(--brand-blue-deep)"/>
        <circle cx="20" cy="20" r="15.5" fill="none" stroke="#fff" stroke-width="2"/>
        <path d="M14 11c1-1 2.5-1 3 .3l1.6 3.6c.4.9 0 1.7-.8 2.2l-1.2.7c.9 2.4 2.3 4.3 4.3 5.8l1-1c.7-.6 1.6-.7 2.3-.1l3 2.4c1 .8.8 2.1-.2 3l-1.4 1.2c-1.2 1-3 1.1-4.5.3C15.800 26.600 12.300 21.900 11.800 16.300c-.1-1.600.6-3.300 2.200-5.300z" fill="#fff"/>
      </svg>
      (08) 5550 1427
    </li>
    <li class="contact__item">
      <svg class="contact__icon" viewBox="0 0 40 40" aria-hidden="true">
        <circle cx="20" cy="20" r="19" fill="var(--brand-blue-deep)"/>
        <circle cx="20" cy="20" r="15.5" fill="none" stroke="#fff" stroke-width="2"/>
        <rect x="13" y="11" width="14" height="7" rx="1" fill="none" stroke="#fff" stroke-width="2"/>
        <rect x="10" y="17" width="20" height="9" rx="2" fill="#fff"/>
        <rect x="14" y="23" width="12" height="6" fill="var(--brand-blue-deep)" stroke="#fff" stroke-width="2"/>
      </svg>
      (08) 5550 1428
    </li>
    <li class="contact__item contact__item--email">
      <svg class="contact__icon" viewBox="0 0 40 40" aria-hidden="true">
        <circle cx="20" cy="20" r="19" fill="var(--brand-blue-deep)"/>
        <circle cx="20" cy="20" r="15.5" fill="none" stroke="#fff" stroke-width="2"/>
        <rect x="11" y="13.500" width="18" height="13" rx="1.500" fill="#fff"/>
        <path d="M11.500 14.500 20 21l8.500-6.500" fill="none" stroke="var(--brand-blue-deep)" stroke-width="1.600"/>
      </svg>
      reception@raybelford.com.au
    </li>
  </ul>

  <address class="address" style="font-style: normal;">
    24 Harrow Lane, Eastmere<br>
    Western Australia 6019
  </address>

  <svg class="footer-band" viewBox="0 0 1200 50" preserveAspectRatio="none" aria-hidden="true">
    <defs>
      <linearGradient id="bandBlue" x1="0" x2="1" y1="0" y2="0">
        <stop offset="0" stop-color="var(--brand-blue-deep)"/>
        <stop offset="0.5" stop-color="var(--brand-blue-light)"/>
        <stop offset="1" stop-color="var(--brand-blue-deep)"/>
      </linearGradient>
      <linearGradient id="bandSilver" x1="0" x2="1" y1="0" y2="0">
        <stop offset="0" stop-color="#8a8a8a"/>
        <stop offset="0.6" stop-color="#e6e6e6"/>
        <stop offset="1" stop-color="#9a9a9a"/>
      </linearGradient>
    </defs>
    <path d="M0 22 Q600 0 1200 22 L1200 50 L0 50 Z" fill="url(#bandSilver)"/>
    <path d="M0 28 Q600 8 1200 28 L1200 50 L0 50 Z" fill="url(#bandBlue)"/>
  </svg>
</main>
</body>
</html>
```